VerdaTurf - 11" x 4" Door Hanger, full color both sides

We need a door hanger designed, 11" x 4", full color both sides, We are a lawn care company that provides lawn mowing, and other services to clients. This door hanger will be place on the 9 neighbors of our current clients. The ad needs to state that we provided lawn service to one of their neighbors today, and that we are in their neighborhood each week on that day. The door hanger will have 4 printings, substituting the day of Tuesday, Wednesday, Thursday, and Friday. All the art work and text will remain the same except the day of the week. For information about VerdaTurf, please visit our website www.verdaturf-example.net. The main emphasis of the message should be that we are their every week on that day, and the benefits to them of using our service (ie. quality time with their family, golf, sports, resting, etc., instead of mowing the lawn). At the bottom of the door hanger will be a coupon offering their tenth (10th) lawn service free, which is the same as a 10% discount.

I have uploaded a template files for the front and back of an 11 x 4 door hanger, The templates are pdf, jpeg, or eps files. The final product can be a pdf, jpeg, or eps file.

Target Market(s)

Neighbors of our existing clients

Industry/Entity Type

Lawn Care

Font styles to use
Serif

Requirements
Must have
• Professional design and art, Short conversational message that relays the following thoughts:
• 1. We mowed your neighbor's lawn today!
• 2. We are in your neighborhood every Tuesday!
• 3. Our lawn service is guaranteed.
• 4. Call to action - Call us today! 512-748-3091
• 5. Of course our contact info, name, phone number, website address.
• 6. Coupon at bottom for "10th lawn service Free!"
Nice to have
• Art work from our website is fine to use, That carries our theme throughout our campaign.
Should not have
• Very wordy. This is basically a billboard, Have very few seconds to grab their attention.

```html
<!DOCTYPE html>
<html lang="en">
<head>
<meta charset="utf-8">
<title>VerdaTurf Door Hanger</title>
<link href="https://fonts.googleapis.com/css2?family=Oswald:wght@400;500;600&family=Source+Sans+3:ital,wght@0,400;0,600;0,700;1,400&display=swap" rel="stylesheet">
<style>
  :root{
    --page:#e8eae4;
    --green-deep:#0f5a1c;
    --green-mid:#1d7a2a;
    --green-bright:#3fa535;
    --green-lime:#8cc63f;
    --green-pale:#b6e07a;
    --yellow:#f3ea2a;
    --white:#ffffff;
    --grass-a:#6fae3a;
    --grass-b:#2f6e1d;
  }
  *{margin:0;padding:0;box-sizing:border-box}
  html,body{width:1164px;height:1200px;overflow:hidden;background:var(--page)}
  body{position:relative;font-family:"Source Sans 3",sans-serif}
  .hanger{
    position:absolute;top:50px;width:400px;height:1100px;
    border-radius:22px;overflow:hidden;
    background:linear-gradient(180deg,var(--green-mid) 0%,var(--green-deep) 60%,var(--green-deep) 100%);
    box-shadow:0 2px 6px rgba(0,0,0,.18);
  }
  .hanger--front{left:150px}
  .hanger--back{left:614px}
  .hanger__art{position:absolute;left:0;top:0;width:400px;height:700px}
  .headline{
    position:absolute;top:22px;left:0;width:100%;text-align:center;
    color:var(--white);font-weight:700;font-size:26px;line-height:1.2;letter-spacing:.2px;
  }
  .brand{
    position:absolute;left:0;width:100%;text-align:center;line-height:1;
    color:var(--white);font-weight:600;font-size:50px;letter-spacing:2px;
  }
  .hanger--front .brand{top:618px}
  .hanger--back .brand{top:642px}
  .tagline{
    position:absolute;top:680px;left:0;width:100%;text-align:center;
    color:var(--yellow);font-style:italic;font-size:25px;line-height:1.3;
  }
  .guarantee{
    position:absolute;top:750px;left:0;width:100%;text-align:center;
    color:var(--white);font-size:18px;line-height:1.2;
  }
  .services{
    position:absolute;top:702px;left:20px;list-style:none;
    color:var(--green-pale);font-size:21px;line-height:31px;font-weight:600;
  }
  .services li{display:flex;align-items:center;gap:10px}
  .services svg{width:16px;height:14px;flex:none}
  .coupon{
    position:absolute;left:24px;width:352px;height:126px;border-radius:12px;overflow:hidden;
    border:2px solid var(--green-pale);
  }
  .hanger--front .coupon{top:790px}
  .hanger--back .coupon{top:866px}
  .coupon__bg{
    position:absolute;inset:0;
    background:linear-gradient(180deg,var(--grass-a) 0%,#5d9f33 45%,var(--grass-b) 100%);
  }
  .coupon__label{
    position:absolute;top:14px;left:146px;color:var(--white);line-height:1;
    font-family:"Oswald",sans-serif;font-weight:500;font-size:24px;letter-spacing:-.3px;
  }
  .coupon__offer{
    position:absolute;top:38px;left:22px;color:var(--white);
    font-family:"Oswald",sans-serif;font-weight:600;line-height:1;white-space:nowrap;
  }
  .coupon__offer .num{font-size:80px;letter-spacing:-3px}
  .coupon__offer .rest{font-size:54px;margin-left:2px}
  .coupon__ribbon{
    position:absolute;top:16px;right:-38px;width:130px;height:20px;
    transform:rotate(45deg);background:var(--green-lime);
    color:var(--white);font-size:12px;font-weight:600;text-align:center;line-height:20px;letter-spacing:1px;
  }
  .cta{position:absolute;color:var(--yellow);font-family:"Oswald",sans-serif;font-weight:400;line-height:1}
  .hanger--front .cta{top:930px;left:0;width:100%;text-align:center;font-size:30px}
  .phone{position:absolute;color:var(--white);font-family:"Oswald",sans-serif;font-weight:500;line-height:1}
  .hanger--front .phone{top:970px;left:0;width:100%;text-align:center;font-size:58px;letter-spacing:1px}
  .call-row{position:absolute;top:1002px;left:18px;display:flex;align-items:baseline;gap:14px}
  .call-row .cta,.call-row .phone{position:static}
  .call-row .cta{font-size:22px}
  .call-row .phone{font-size:42px;letter-spacing:1px}
  .web{
    position:absolute;bottom:0;left:0;width:100%;height:46px;background:var(--white);
    color:var(--green-deep);font-weight:600;font-size:22px;text-align:center;line-height:46px;
  }
</style>
</head>
<body>

<section class="hanger hanger--front">
  <svg class="hanger__art" viewBox="0 0 400 700">
    <defs>
      <linearGradient id="mowGrass" x1="0" y1="0" x2="0" y2="1">
        <stop offset="0" stop-color="#7aa84a"/><stop offset=".5" stop-color="#4f8a2c"/><stop offset="1" stop-color="#3b6f22"/>
      </linearGradient>
      <linearGradient id="yardPhoto" x1="0" y1="0" x2="0" y2="1">
        <stop offset="0" stop-color="#c9b79a"/><stop offset=".45" stop-color="#b06a5a"/><stop offset="1" stop-color="#6fc23a"/>
      </linearGradient>
    </defs>
    <path d="M0,262 Q140,140 400,130 L400,150 Q160,160 0,290 Z" fill="var(--green-bright)"/>
    <path d="M0,290 Q160,160 400,150 L400,165 Q170,175 0,310 Z" fill="var(--green-pale)"/>
    <path d="M0,310 Q170,175 400,165 L400,500 Q220,590 0,585 Z" fill="url(#mowGrass)" role="img" aria-label="Photo of a red lawn mower cutting thick green grass"/>
    <path d="M0,585 Q220,590 400,500 L400,520 Q230,610 0,605 Z" fill="var(--green-lime)"/>
    <circle cx="292" cy="500" r="102" fill="var(--green-deep)"/>
    <circle cx="292" cy="500" r="96" fill="var(--white)"/>
    <circle cx="292" cy="500" r="91" fill="url(#yardPhoto)" role="img" aria-label="Photo of a house porch with flower beds and a trimmed lawn"/>
    <circle cx="200" cy="165" r="68" fill="var(--green-mid)"/>
    <circle cx="200" cy="165" r="62" fill="var(--page)"/>
  </svg>
  <h2 class="headline">WE MOWED YOUR NEIGHBOR'S<br>LAWN TODAY!</h2>
  <h1 class="brand">VERDATURF</h1>
  <p class="tagline">We are in your<br>neighborhood every Tuesday!</p>
  <p class="guarantee">Our lawn service is guaranteed.</p>
  <div class="coupon">
    <div class="coupon__bg" role="img" aria-label="Close-up photo of green grass blades"></div>
    <span class="coupon__label">LAWN SERVICE</span>
    <span class="coupon__offer"><span class="num">10</span><span class="rest">TH FREE!</span></span>
    <span class="coupon__ribbon">DISCOUNT</span>
  </div>
  <p class="cta">CALL US TODAY!</p>
  <p class="phone">512-748-3091</p>
  <p class="web">www.verdaturf-example.net</p>
</section>

<section class="hanger hanger--back">
  <svg class="hanger__art" viewBox="0 0 400 700">
    <defs>
      <linearGradient id="frontYard" x1="0" y1="0" x2="0" y2="1">
        <stop offset="0" stop-color="#3e5a3a"/><stop offset=".35" stop-color="#8a4a4a"/><stop offset=".5" stop-color="#6fbf3a"/><stop offset="1" stop-color="#5aa82c"/>
      </linearGradient>
      <linearGradient id="handGrass" x1="0" y1="0" x2="0" y2="1">
        <stop offset="0" stop-color="#8fc85a"/><stop offset=".5" stop-color="#d9b89a"/><stop offset="1" stop-color="#3f8a26"/>
      </linearGradient>
    </defs>
    <path d="M0,262 Q140,150 400,140 L400,160 Q160,170 0,290 Z" fill="var(--green-bright)"/>
    <path d="M0,290 Q160,170 400,160 L400,175 Q170,185 0,310 Z" fill="var(--green-pale)"/>
    <path d="M0,310 Q170,185 400,175 L400,530 Q220,610 0,600 Z" fill="url(#frontYard)" role="img" aria-label="Photo of a front yard with a lush lawn, shrubs, flowers and a dark front door"/>
    <path d="M0,600 Q220,610 400,530 L400,550 Q230,630 0,620 Z" fill="var(--green-lime)"/>
    <circle cx="302" cy="530" r="98" fill="var(--green-deep)"/>
    <circle cx="302" cy="530" r="92" fill="var(--white)"/>
    <circle cx="302" cy="530" r="87" fill="url(#handGrass)" role="img" aria-label="Photo of a hand resting on soft green grass"/>
    <circle cx="200" cy="180" r="68" fill="var(--green-mid)"/>
    <circle cx="200" cy="180" r="62" fill="var(--page)"/>
  </svg>
  <h2 class="headline">WE MOWED YOUR NEIGHBOR'S<br>LAWN TODAY!</h2>
  <h1 class="brand">VERDATURF</h1>
  <ul class="services">
    <li><svg viewBox="0 0 16 14"><path d="M1,7 L6,12 L15,2" fill="none" stroke="var(--yellow)" stroke-width="2.5"/></svg>Weekly or bi-weekly lawn mowing</li>
    <li><svg viewBox="0 0 16 14"><path d="M1,7 L6,12 L15,2" fill="none" stroke="var(--yellow)" stroke-width="2.5"/></svg>Fertilization &amp; weed-control programs</li>
    <li><svg viewBox="0 0 16 14"><path d="M1,7 L6,12 L15,2" fill="none" stroke="var(--yellow)" stroke-width="2.5"/></svg>Landscape services</li>
    <li><svg viewBox="0 0 16 14"><path d="M1,7 L6,12 L15,2" fill="none" stroke="var(--yellow)" stroke-width="2.5"/></svg>Sprinkler repair</li>
    <li><svg viewBox="0 0 16 14"><path d="M1,7 L6,12 L15,2" fill="none" stroke="var(--yellow)" stroke-width="2.5"/></svg>Landscape lighting</li>
  </ul>
  <div class="coupon">
    <div class="coupon__bg" role="img" aria-label="Close-up photo of green grass blades"></div>
    <span class="coupon__label">LAWN SERVICE</span>
    <span class="coupon__offer"><span class="num">10</span><span class="rest">TH FREE!</span></span>
    <span class="coupon__ribbon">DISCOUNT</span>
  </div>
  <div class="call-row">
    <p class="cta">CALL US TODAY!</p>
    <p class="phone">512-748-3091</p>
  </div>
  <p class="web">www.verdaturf-example.net</p>
</section>

</body>
</html>
```